Just Sold Postcard

Real Estate/ Bramwell Oakes Realty.I'd like a template that I can use to change out the picture of the home, verbiage on the front, and address. I'm including a picture of what I've used in the past. I like designs that use red, with some blue and white. I'd like the ability to change the verbiage on the back as well.

Industry/Entity Type

Real Estate

Font styles to use
Serif
Sans Serif

```html
<!DOCTYPE html>
<html lang="en">
<head>
<meta charset="utf-8">
<title>Just Sold Postcard – Bramwell Oakes Realty</title>
<link rel="stylesheet" href="https://fonts.googleapis.com/css2?family=Roboto+Condensed:ital,wght@0,400;0,700;1,400;1,700&family=Roboto:wght@400;700&display=swap">
<style>
  :root {
    --red: #d71f26;
    --red-dark: #a5121a;
    --navy: #2b2f7a;
    --navy-dark: #1f2260;
    --white: #ffffff;
    --paper: #f4f4f4;
    --ink: #1c1c1c;
    --stage: #e9e7e4;
  }
  * { margin: 0; padding: 0; box-sizing: border-box; }
  html, body { width: 900px; height: 1200px; overflow: hidden; }
  body {
    background: var(--stage);
    position: relative;
    font-family: "Roboto Condensed", "Roboto", sans-serif;
    color: var(--ink);
  }

  /* ---------- Front ---------- */
  .card-front {
    position: absolute; left: 128px; top: 57px;
    width: 645px; height: 500px; overflow: hidden;
    background: var(--white);
    box-shadow: 0 4px 12px rgba(0,0,0,.25);
  }
  .top-band {
    position: absolute; left: 0; top: 0; width: 100%; height: 40px;
    background: linear-gradient(var(--red), var(--red-dark));
  }
  .home-photo {
    position: absolute; left: 0; top: 40px; width: 100%; height: 460px;
    background: linear-gradient(180deg, #c9d9e8 0%, #a7b3a2 18%, #9a4a3a 35%, #8c3f30 62%, #6f8a52 80%, #4f8a33 100%);
  }
  .info-pennant {
    position: absolute; left: 30px; top: 40px; width: 247px; height: 400px;
  }
  .info-pennant svg { position: absolute; inset: 0; }
  .info-content {
    position: absolute; left: 30px; top: 40px; width: 247px;
    text-align: center; color: var(--navy);
  }
  .brand {
    display: flex; align-items: center; justify-content: center; gap: 7px;
    margin-top: 20px;
    font-family: "Roboto Condensed", sans-serif; font-weight: 700;
    font-size: 22px; color: var(--red);
  }
  .brand-mark { width: 12px; height: 12px; background: var(--navy); }
  .address {
    margin-top: 34px; font-size: 15px; font-weight: 700; letter-spacing: .3px;
  }
  .description {
    margin-top: 14px; font-size: 14px; font-style: italic; line-height: 18px; color: var(--ink);
  }
  .agent {
    margin-top: 20px; font-size: 18px; line-height: 22px;
  }
  .phone-bar {
    position: absolute; left: 22px; top: 303px; width: 265px; height: 50px;
    background: linear-gradient(var(--red), var(--red-dark));
    display: flex; align-items: center; justify-content: center; gap: 12px;
    color: var(--white); font-weight: 700; font-size: 30px;
    box-shadow: 0 3px 5px rgba(0,0,0,.35);
  }
  .sold-sign {
    position: absolute; left: 455px; top: 380px; width: 144px; height: 60px;
    background: linear-gradient(var(--red), var(--red-dark));
    border-radius: 4px; text-align: center; color: var(--white);
    text-transform: uppercase; font-weight: 700;
    box-shadow: 0 2px 5px rgba(0,0,0,.4);
  }
  .sold-sign .headline { font-size: 25px; line-height: 28px; margin-top: 5px; }
  .sold-sign .subline { font-size: 15px; line-height: 17px; }
  .sign-post {
    position: absolute; left: 521px; top: 362px; width: 12px; height: 138px;
    background: #7a3c22;
  }

  /* ---------- Back ---------- */
  .card-back {
    position: absolute; left: 127px; top: 640px;
    width: 648px; height: 502px; overflow: hidden;
    background: var(--white);
    box-shadow: 0 4px 12px rgba(0,0,0,.25);
  }
  .promo-panel {
    position: absolute; left: 0; top: 0; width: 305px; height: 100%;
    background: linear-gradient(180deg, var(--white), var(--paper));
  }
  .promo-panel .brand { margin-top: 42px; font-size: 28px; }
  .promo-panel .brand-mark { width: 14px; height: 14px; }
  .roof { position: absolute; left: 0; top: 125px; width: 305px; height: 70px; }
  .promo-block {
    position: absolute; left: 0; top: 190px; width: 305px; height: 312px;
    background: linear-gradient(var(--navy), var(--navy-dark));
  }
  .promo-rule {
    position: absolute; left: 0; width: 305px; height: 2px; background: var(--white);
  }
  .offer {
    position: absolute; left: 0; top: 235px; width: 305px; text-align: center;
    font-weight: 700;
  }
  .offer .lead, .offer .tail { color: var(--red); font-size: 21px; line-height: 25px; }
  .offer .main { color: var(--white); font-size: 38px; line-height: 44px; }
  .contact-band {
    position: absolute; left: 0; top: 413px; width: 320px; height: 60px;
    background: var(--white); box-shadow: 0 2px 5px rgba(0,0,0,.3);
    padding: 6px 0 0 30px;
  }
  .contact-row { display: flex; align-items: center; gap: 12px; }
  .contact-row.phone { color: var(--red); font-size: 31px; font-weight: 700; line-height: 34px; }
  .contact-row.email { color: var(--navy-dark); font-family: "Roboto", sans-serif; font-size: 13px; font-weight: 700; }
  .divider-line {
    position: absolute; left: 310px; top: 0; width: 5px; height: 100%;
    background: var(--red); border-left: 2px solid var(--white);
  }
  .stamp-box {
    position: absolute; left: 510px; top: 43px; width: 96px; height: 95px;
    border: 2px solid var(--ink);
  }
  .address-line {
    position: absolute; left: 348px; width: 245px; height: 2px; background: var(--ink);
  }
</style>
</head>
<body>

<!-- Front of postcard -->
<section class="card-front">
  <div class="top-band"></div>
  <div class="home-photo" role="img" aria-label="Photo of the sold home: two-storey red brick house with a lawn and shrubs"></div>

  <div class="info-pennant">
    <svg width="247" height="400" viewBox="0 0 247 400">
      <polygon points="0,0 247,0 247,400 123,370 0,400" fill="rgba(255,255,255,0.82)"/>
    </svg>
  </div>

  <div class="info-content">
    <div class="brand"><span class="brand-mark"></span>Bramwell Oakes Realty</div>
    <p class="address">2715 WILLOW CREST DRIVE</p>
    <p class="description">Fabulous End Unit With granite<br>countertops and hardwood floors<br>Private lot</p>
    <p class="agent">Marla Jennings<br>your Neighborhood Expert</p>
  </div>

  <div class="phone-bar">
    <svg width="22" height="22" viewBox="0 0 22 22" aria-hidden="true">
      <rect width="22" height="22" rx="4" fill="#fff"/>
      <path d="M7 5c1 0 2 2 2 3s-1 1-1 2 2 3 3 4 1-1 2-1 3 1 3 2-1 2-2 2C9 17 5 13 5 7c0-1 1-2 2-2z" fill="#d71f26"/>
    </svg>
    919-555-0142
  </div>

  <div class="sign-post"></div>
  <div class="sold-sign">
    <div class="headline">Just Sold</div>
    <div class="subline">Brought Buyer</div>
  </div>
</section>

<!-- Back of postcard -->
<section class="card-back">
  <div class="promo-panel">
    <div class="brand"><span class="brand-mark"></span>Bramwell Oakes</div>
  </div>

  <svg class="roof" viewBox="0 0 305 70" preserveAspectRatio="none" aria-hidden="true">
    <polygon points="0,40 160,0 305,40 305,70 0,70" fill="#a5121a"/>
    <polygon points="0,55 160,18 305,55 305,70 0,70" fill="#2b2f7a"/>
  </svg>

  <div class="promo-block"></div>
  <div class="promo-rule" style="top:220px"></div>
  <div class="promo-rule" style="top:350px"></div>

  <div class="offer">
    <div class="lead">Contact me today! For a</div>
    <div class="main">FREE MARKET</div>
    <div class="tail">Analysis of your home!</div>
  </div>

  <div class="contact-band">
    <div class="contact-row phone">
      <svg width="20" height="20" viewBox="0 0 22 22" aria-hidden="true">
        <rect width="22" height="22" rx="4" fill="#d71f26"/>
        <path d="M7 5c1 0 2 2 2 3s-1 1-1 2 2 3 3 4 1-1 2-1 3 1 3 2-1 2-2 2C9 17 5 13 5 7c0-1 1-2 2-2z" fill="#fff"/>
      </svg>
      919-555-0142
    </div>
    <div class="contact-row email">
      <svg width="20" height="12" viewBox="0 0 20 12" aria-hidden="true">
        <rect width="20" height="12" fill="#d71f26"/>
        <path d="M1 1l9 6 9-6" stroke="#fff" stroke-width="1.5" fill="none"/>
      </svg>
      jennings.marla@example.com
    </div>
  </div>

  <div class="divider-line"></div>
  <div class="stamp-box"></div>
  <div class="address-line" style="top:261px"></div>
  <div class="address-line" style="top:294px"></div>
  <div class="address-line" style="top:333px"></div>
</section>

</body>
</html>
```